"Velmaro" sparkling beverage

Dear All!
I need a stick label (82*95 - front label, 82*65 - back label )design for а sparkling beverage, name is "Velmaro", 4 flavours: lemonade,duchess pear, estragon, original. Transparent glass bottles 0,5 liter (alumnium closure 28*15)/0,33 liter (crown cap), neck label should also be on the bottle 0,5 liter.
European style is welcomed
Do not send the disigns with a little changes several times, please!!!
Young people from 12-30 ages old

```html
<!DOCTYPE html>
<html lang="en">
<head>
<meta charset="utf-8">
<title>Velmaro — flavour labels</title>
<link rel="stylesheet" href="https://fonts.googleapis.com/css2?family=Lobster&family=Cormorant+SC:wght@500&display=swap">
<style>
  :root {
    --page: #eeeae4;
    --night: #1b2140;
    --night-deep: #121733;
    --smoke: #6b4a3c;
    --smoke-light: #8a6a58;
    --estragon: #9fd13a;
    --estragon-text: #c4e24a;
    --lemon: #f29a1c;
    --lemon-text: #f6b52a;
    --volume: #e9e2d0;
  }
  * { margin: 0; padding: 0; box-sizing: border-box; }
  html, body {
    width: 1200px;
    height: 930px;
    overflow: hidden;
    background: var(--page);
  }
  .label-sheet {
    position: relative;
    width: 1200px;
    height: 930px;
    display: flex;
    justify-content: center;
    align-items: center;
    gap: 40px;
  }
  .label {
    position: relative;
    width: 540px;
    height: 453px;
    overflow: hidden;
    background: var(--night);
    box-shadow: 0 6px 24px rgba(0, 0, 0, 0.18);
  }
  .label__backdrop {
    position: absolute;
    inset: 0;
    background:
      radial-gradient(ellipse 60% 35% at 30% 60%, var(--smoke-light) 0%, transparent 70%),
      radial-gradient(ellipse 55% 40% at 75% 40%, var(--smoke) 0%, transparent 70%),
      radial-gradient(ellipse 45% 30% at 20% 90%, var(--smoke) 0%, transparent 70%),
      linear-gradient(160deg, var(--night) 0%, var(--night-deep) 100%);
  }
  .label__emblem {
    position: absolute;
    left: 100px;
    top: 18px;
    width: 220px;
    height: 70px;
    border-radius: 4px;
    opacity: 0.35;
  }
  .label--estragon .label__emblem { background: linear-gradient(90deg, transparent, var(--estragon), transparent); }
  .label--lemonade .label__emblem { background: linear-gradient(90deg, transparent, var(--lemon), transparent); }
  .label__brand {
    position: absolute;
    left: 0;
    right: 0;
    top: 120px;
    text-align: center;
    font-family: "Lobster", cursive;
    font-weight: 400;
    font-size: 92px;
    line-height: 1;
    letter-spacing: 2px;
  }
  .label--estragon .label__brand { color: var(--estragon); }
  .label--lemonade .label__brand { color: var(--lemon); }
  .label__produce {
    position: absolute;
    left: 190px;
    top: 150px;
    width: 240px;
    height: 110px;
    border-radius: 50%;
    opacity: 0.85;
  }
  .label--estragon .label__produce { background: radial-gradient(ellipse at center, #5e8a3a 0%, #3d5e2a 55%, transparent 75%); }
  .label--lemonade .label__produce { background: radial-gradient(ellipse at center, #ffe34a 0%, #f2c21a 55%, transparent 75%); }
  .label__flavour {
    position: absolute;
    left: 0;
    right: 0;
    top: 318px;
    text-align: center;
    font-family: "Lobster", cursive;
    font-size: 54px;
    line-height: 1;
  }
  .label--estragon .label__flavour { color: var(--estragon-text); }
  .label--lemonade .label__flavour { color: var(--lemon-text); }
  .label__volume {
    position: absolute;
    left: 0;
    right: 0;
    top: 388px;
    text-align: center;
    font-family: "Cormorant SC", serif;
    font-weight: 500;
    font-size: 30px;
    color: var(--volume);
    letter-spacing: 1px;
  }
</style>
</head>
<body>
  <main class="label-sheet">
    <section class="label label--estragon">
      <div class="label__backdrop" role="img" aria-label="Starry night sky with drifting brown smoke"></div>
      <div class="label__emblem" role="img" aria-label="Green line drawing of a telescope"></div>
      <div class="label__produce" role="img" aria-label="Sprig of fresh tarragon"></div>
      <h2 class="label__brand">Velmaro</h2>
      <p class="label__flavour">Estragon</p>
      <p class="label__volume">500ml</p>
    </section>
    <section class="label label--lemonade">
      <div class="label__backdrop" role="img" aria-label="Starry night sky with drifting brown smoke"></div>
      <div class="label__emblem" role="img" aria-label="Orange line drawing of a telescope"></div>
      <div class="label__produce" role="img" aria-label="Whole and halved fresh lemons"></div>
      <h2 class="label__brand">Velmaro</h2>
      <p class="label__flavour">Lemonade</p>
      <p class="label__volume">500ml</p>
    </section>
  </main>
</body>
</html>
```